Cyber Security Services Flyer/Datasheet

We are looking for a revamp of our current "Cyber Security Penetration Testing Services Datasheet". We would like a professional/modern datasheet that we can give to our Australian customers that are small to mid-sized business owners.

Please see the attached file "PLEASE READ ME.docx" for more details about the design project. It includes all of the design information. If you have more questions or would like to ask any questions please feel free to ask, we are happy to help.

```html
<!DOCTYPE html>
<html lang="en">
<head>
<meta charset="utf-8">
<title>Bastion Cyber – Penetration Testing Datasheet</title>
<link href="https://fonts.googleapis.com/css2?family=Bebas+Neue&family=Montserrat:wght@400;500;600;700&display=swap" rel="stylesheet">
<style>
:root{
  --navy:#0d0930;
  --sky:#29a3dc;
  --pill:#3a5b94;
  --pill-dark:#2c4678;
  --ink:#1f1f2a;
  --white:#ffffff;
  --halo:#eef0f4;
}
*{margin:0;padding:0;box-sizing:border-box}
html,body{width:1200px;height:1200px;overflow:hidden;background:var(--white);font-family:"Montserrat",sans-serif;color:var(--ink)}
.sheet{position:absolute;left:242px;top:94px;width:722px;height:1020px;background:var(--white);overflow:hidden}
.abs{position:absolute}
.header-art{position:absolute;left:0;top:0;width:722px;height:306px}
.brand{position:absolute;left:30px;top:64px;display:flex;align-items:center;gap:6px;color:var(--white);font-weight:700;font-size:14px;letter-spacing:1px}
.brand-dot{width:10px;height:10px;border-radius:50%;background:var(--white)}
.tagline{position:absolute;left:40px;top:134px;color:var(--white);font-size:19.5px;font-weight:400;letter-spacing:.8px;line-height:27px}
.headline{position:absolute;left:40px;top:192px;color:var(--white);font-family:"Bebas Neue",sans-serif;font-size:58px;line-height:48px;letter-spacing:.3px}
.section-title{position:absolute;color:var(--sky);font-weight:700;font-size:17.5px;letter-spacing:.4px}
.service{position:absolute;left:41px;display:flex;align-items:center;gap:12px;font-size:12.5px;font-weight:500;letter-spacing:.2px}
.icon-disc{width:39px;height:39px;border-radius:50%;background:var(--pill);border:3px solid var(--sky);display:flex;align-items:center;justify-content:center;flex:none}
.icon-disc svg{width:18px;height:18px}
.why-copy{position:absolute;left:377px;top:368px;width:296px;font-size:9.3px;line-height:11.6px}
.benefit{position:absolute;display:flex;align-items:center;gap:9px;font-size:12.3px;line-height:14.6px}
.method-art{position:absolute;left:0;top:640px;width:722px;height:310px}
.method-core{position:absolute;left:67px;top:712px;width:175px;height:175px;border-radius:50%;background:linear-gradient(180deg,#3a6aa3,#29a3dc);color:var(--white);text-align:center;padding:36px 24px 0}
.method-core h3{font-size:10.5px;font-weight:700;line-height:13px}
.method-core p{font-size:9.2px;line-height:11px;font-weight:400}
.step{position:absolute;height:43px;border-radius:22px;background:var(--pill);border:2px solid var(--pill-dark);color:var(--white);display:flex;align-items:center;padding-left:4px}
.step-icon{width:31px;height:31px;border-radius:50%;background:var(--white);border:2px solid var(--sky);flex:none;display:flex;align-items:center;justify-content:center;margin-right:8px}
.step-icon svg{width:17px;height:17px}
.step h4{font-size:11px;font-weight:700;letter-spacing:.3px;line-height:12px}
.step p{font-size:6.6px;line-height:7.4px;padding-right:12px}
.footer-art{position:absolute;left:0;top:946px;width:722px;height:74px}
.contact{position:absolute;left:40px;color:var(--white);font-size:14.4px;display:flex;align-items:center;gap:7px}
.contact svg{width:10px;height:10px}
.social{position:absolute;left:661px;top:963px;width:22px;height:22px;border-radius:50%;background:var(--sky)}
</style>
</head>
<body>
<main class="sheet">

  <svg class="header-art" viewBox="0 0 722 306">
    <defs>
      <radialGradient id="glow" cx="72%" cy="45%" r="70%">
        <stop offset="0" stop-color="#2a6fd6"/>
        <stop offset=".45" stop-color="#0f2f8a"/>
        <stop offset="1" stop-color="#07124a"/>
      </radialGradient>
    </defs>
    <rect width="722" height="306" fill="var(--navy)"/>
    <polygon points="370,0 374,0 330,306 326,306" fill="#ffffff"/>
    <polygon points="378,0 722,0 722,306 334,306" fill="url(#glow)" role="img" aria-label="Glowing digital padlock illustration over circuit lines"/>
  </svg>

  <div class="brand"><span class="brand-dot"></span>BASTION CYBER</div>
  <div class="tagline">AFFORDABLE SECURITY<br>ASSESSMENTS TO SUIT</div>
  <div class="headline">YOUR BUSINESS<br>REQUIREMENTS</div>

  <h2 class="section-title" style="left:40px;top:331px">OUR SERVICES</h2>

  <div class="service" style="top:361px"><span class="icon-disc"><svg viewBox="0 0 20 20" fill="none" stroke="#fff" stroke-width="2"><rect x="3" y="6" width="11" height="11"/><path d="M9 11l8-8M12 3h5v5"/></svg></span>External Penetration Testing</div>
  <div class="service" style="top:405px"><span class="icon-disc"><svg viewBox="0 0 20 20" fill="#fff"><circle cx="6" cy="8" r="2.5"/><circle cx="14" cy="8" r="2.5"/><rect x="2" y="12" width="8" height="6" rx="2"/><rect x="10" y="12" width="8" height="6" rx="2"/></svg></span>Internal Penetration Testing</div>
  <div class="service" style="top:449px"><span class="icon-disc"><svg viewBox="0 0 20 20" fill="none" stroke="#fff" stroke-width="2"><rect x="3" y="3" width="14" height="14" rx="1"/><path d="M3 7h14"/></svg></span>Web Application Testing</div>
  <div class="service" style="top:491px"><span class="icon-disc"><svg viewBox="0 0 20 20" fill="none" stroke="#fff" stroke-width="1.8"><circle cx="10" cy="9" r="1.5" fill="#fff"/><path d="M10 10v8M6.5 5.5a5 5 0 0 0 0 7M13.5 5.5a5 5 0 0 1 0 7M4 3a8.5 8.5 0 0 0 0 12M16 3a8.5 8.5 0 0 1 0 12"/></svg></span>Wireless Penetration Test</div>
  <div class="service" style="top:532px"><span class="icon-disc"><svg viewBox="0 0 20 20" fill="none" stroke="#fff" stroke-width="2"><rect x="2" y="4" width="16" height="12"/><path d="M2 4l8 7 8-7"/></svg></span>Phishing Penetration Testing</div>
  <div class="service" style="top:576px"><span class="icon-disc"><svg viewBox="0 0 20 20" fill="none" stroke="#fff" stroke-width="2"><circle cx="8" cy="8" r="5"/><path d="M12 12l6 6"/></svg></span>Vulnerability Assessments</div>

  <h2 class="section-title" style="left:375px;top:331px">WHY PENETRATION TESTING</h2>
  <p class="why-copy">Penetration Testing is the process of simulating real-world attacks by using the same techniques as malicious hackers. Penetration Testing is one of the most comprehensive ways for organisations to develop an understanding of the level of cyber security risk that they carry. Understanding these risks allows organisations to meet industry compliance and regulatory requirements. Additionally, penetration testing allows organisations to develop strategies for the management and remediation of vulnerabilities to reduce overall risk to their business and sensitive data.</p>

  <div class="benefit" style="left:373px;top:502px"><span class="icon-disc"><svg viewBox="0 0 20 20" fill="#fff"><path d="M10 2l7 3v5c0 4-3 7-7 8-4-1-7-4-7-8V5z"/><path d="M7 10l2 2 4-4" stroke="var(--pill)" stroke-width="1.8" fill="none"/></svg></span>Proactively<br>defend against<br>cyber attacks</div>
  <div class="benefit" style="left:534px;top:502px"><span class="icon-disc"><svg viewBox="0 0 20 20" fill="none" stroke="#fff" stroke-width="1.8"><rect x="3" y="3" width="5" height="14"/><path d="M13 3v14M10.5 6L13 3l2.5 3M10.5 14l2.5 3 2.5-3"/></svg></span>Set a baseline for<br>your security<br>program</div>
  <div class="benefit" style="left:373px;top:575px"><span class="icon-disc"><svg viewBox="0 0 20 20" fill="none" stroke="#fff" stroke-width="1.8"><circle cx="10" cy="10" r="7"/><path d="M7 10l2 2 4-4"/></svg></span>Meet compliance<br>standards</div>
  <div class="benefit" style="left:534px;top:572px"><span class="icon-disc"><svg viewBox="0 0 20 20" fill="none" stroke="#fff" stroke-width="1.8"><path d="M3 3v14h14M6 13l4-4 3 3 4-5"/></svg></span>Improve your<br>overall security<br>posture</div>

  <h2 class="section-title" style="left:40px;top:628px">OUR METHODOLOGY</h2>

  <svg class="method-art" viewBox="0 640 722 310" fill="none">
    <circle cx="154" cy="799" r="112" fill="var(--halo)"/>
    <circle cx="154" cy="799" r="101" fill="#ffffff"/>
    <path d="M151 685 A114 114 0 0 1 151 913" stroke="var(--navy)" stroke-width="1.6"/>
    <circle cx="151" cy="685" r="5" fill="var(--sky)"/>
    <circle cx="151" cy="913" r="5" fill="var(--sky)"/>
    <g stroke="#333" stroke-width="1" stroke-dasharray="3 2">
      <path d="M218 692 L285 666 L301 668"/>
      <path d="M262 735 L270 724 L330 725"/>
      <path d="M279 808 L360 796"/>
      <path d="M256 871 L265 876 L339 849"/>
      <path d="M205 915 L290 924 L301 918"/>
    </g>
    <g fill="var(--sky)" stroke="#fff" stroke-width="2">
      <circle cx="210" cy="696" r="11"/>
      <circle cx="254" cy="741" r="11"/>
      <circle cx="269" cy="810" r="11"/>
      <circle cx="248" cy="867" r="11"/>
      <circle cx="197" cy="906" r="11"/>
    </g>
    <g fill="#fff" font-family="Montserrat, sans-serif" font-size="10" font-weight="700" text-anchor="middle">
      <text x="210" y="700">1</text><text x="254" y="745">2</text><text x="269" y="814">3</text><text x="248" y="871">4</text><text x="197" y="910">5</text>
    </g>
  </svg>

  <div class="method-core">
    <h3>OUR<br>METHODOLOGY</h3>
    <p>NetWarden uses a mix of manual and automated testing techniques in an attempt to gain access to the system and/or sensitive data on the system</p>
  </div>

  <div class="step" style="left:301px;top:645px;width:319px"><span class="step-icon"><svg viewBox="0 0 20 20" fill="none" stroke="var(--pill)" stroke-width="1.6"><circle cx="10" cy="10" r="7"/><circle cx="10" cy="10" r="3"/><path d="M10 1v18M1 10h18"/></svg></span><div><h4>SCOPE</h4><p>A penetration test engagement includes specific asset criteria described by the customer. At this stage we also discuss specific threat models and capture your business objectives.</p></div></div>

  <div class="step" style="left:330px;top:710px;width:320px"><span class="step-icon"><svg viewBox="0 0 20 20" fill="none" stroke="var(--pill)" stroke-width="1.6"><rect x="6" y="9" width="8" height="6"/><path d="M7.5 9V7a2.5 2.5 0 0 1 5 0v2"/><circle cx="10" cy="10" r="8.5"/></svg></span><div><h4>INITIAL ACCESS</h4><p>Using information reconnaissance, social engineering or physical access, breaching the environment as per the scope objectives.</p></div></div>

  <div class="step" style="left:360px;top:775px;width:321px"><span class="step-icon"><svg viewBox="0 0 20 20" fill="none" stroke="var(--pill)" stroke-width="1.8"><path d="M10 2v16M2 10h16M7.5 4.5L10 2l2.5 2.5M7.5 15.5L10 18l2.5-2.5M4.5 7.5L2 10l2.5 2.5M15.5 7.5L18 10l-2.5 2.5"/></svg></span><div><h4>ESCALATION AND LATERAL MOVEMENT</h4><p>The initial foothold is expanded in the environment via various lateral movement techniques to explicitly bypass security defences.</p></div></div>

  <div class="step" style="left:339px;top:838px;width:311px"><span class="step-icon"><svg viewBox="0 0 20 20" fill="none" stroke="var(--pill)" stroke-width="1.6"><circle cx="10" cy="10" r="7.5"/><circle cx="10" cy="10" r="4"/><path d="M10 10l7 7"/></svg></span><div><h4>ACTION ON OBJECTIVE</h4><p>Sensitive data capture and exfiltration from controlled environment is tested during this phase.</p></div></div>

  <div class="step" style="left:301px;top:900px;width:322px"><span class="step-icon"><svg viewBox="0 0 20 20" fill="var(--pill)"><path d="M4 2h8l4 4v12H4z"/><rect x="7" y="11" width="2" height="5" fill="#fff"/><rect x="10" y="9" width="2" height="7" fill="#fff"/><rect x="13" y="12" width="1.5" height="4" fill="#fff"/></svg></span><div><h4>REPORTING AND DEBRIEF</h4><p>A detailed report of various attack chains used to compromise, defences found and triggered, and recommendations are given to improve your business' security posture.</p></div></div>

  <svg class="footer-art" viewBox="0 946 722 74">
    <polygon points="319,997 722,997 722,1020 330,1020" fill="var(--sky)"/>
    <polygon points="0,946 298,946 327,1020 0,1020" fill="var(--navy)"/>
  </svg>

  <div class="contact" style="top:951px"><svg viewBox="0 0 10 10" fill="none" stroke="#fff" stroke-width="1"><circle cx="5" cy="5" r="4.3"/><path d="M.7 5h8.6M5 .7c-2 2.4-2 6.2 0 8.6M5 .7c2 2.4 2 6.2 0 8.6"/></svg>www.bastioncyber.com.au</div>
  <div class="contact" style="top:971px"><svg viewBox="0 0 10 10" fill="#fff"><rect x=".5" y="2" width="9" height="6"/><path d="M.5 2l4.5 3.5L9.5 2" stroke="var(--navy)" stroke-width=".8" fill="none"/></svg>hello@bastioncyber.com.au</div>

  <span class="social" aria-label="Social profile"></span>
</main>
</body>
</html>
```